CSS design for a web application

We are currently building a web application in JAVA. The application uses a combination of a HTML template and CSS for the look and feel. We currenly have a very corporate look and feel for demo puposes, but we need to have some CSS designs that we can show to prospective customers. One of the functionalities of our application is the possibility to upload a customer's own (CSS) design in the application.

Our first customer is a high school in The Netherlands (12-18 year students) for children who are physically challenged. So the design should be easy to read, buttons should be easy to see, read and click and the different parts/texts on the website shouldn't be too close together. At the same time, we would like to avoid too much scrolling (especially horizontally). Go with a minimun screen resolution of 1024 x 768.

As our users are children, nice colours and other fun elements would be nice, while keeping a 'school like' appearance. Please use pictures and icons that our users will relate too. We want to communicate that our software is easy, fun and at the same time professional.

Our product is based on Brindle Suite by Brindle and thus Brindle applications as Postrix, Calendar, Brindle Pages etc are all integrated in our software solution.

Find attached a static HTML file that contains our current CSS design. This should be used as a basis as it contains al the CSS elements that are used in the application. Please note that jQuery (javascript) knowledge is necessary.

Target Market(s)

Students at high school (age group 12/13 to 17/18). Users have physical disabilities that sometimes means they need special equipment/tools to operate their laptop.

Requirements
Must have
• Easy too navigate, buttons that are easy to see/use
Nice to have
• 'WOW' factor when people look at the design
Should not have
• buttons/text that is too small, too close together

```html
<!DOCTYPE html>
<html lang="nl">
<head>
<meta charset="utf-8">
<title>Study guide Engels – Skylark</title>
<link rel="stylesheet" href="https://fonts.googleapis.com/css2?family=Nunito:wght@700;800;900&family=Open+Sans:wght@400;600&display=swap">
<style>
:root{
  --page:#870808;
  --tab-tan:#d8a052;
  --tab-tan-dark:#b97a2e;
  --out-yellow:#f7d41a;
  --welcome-red:#9c0a0a;
  --tab-blue:#1d5f9c;
  --nav-yellow:#fbee5a;
  --nav-yellow-light:#fff9b8;
  --nav-text:#1a5a96;
  --green:#7fae3a;
  --green-dark:#5f8f22;
  --purple:#9574cb;
  --row-gap:#ece48e;
  --row:#ffffff;
  --panel-bottom:#fbf5cf;
  --white:#ffffff;
  --ink:#111111;
}
*{box-sizing:border-box;margin:0;padding:0}
html,body{width:1200px;height:610px;overflow:hidden}
body{background:var(--page);font-family:"Open Sans",Verdana,sans-serif;color:var(--ink);position:relative}
.abs{position:absolute}

.brand{left:18px;top:8px;display:flex;align-items:center;gap:8px}
.brand-dot{width:30px;height:30px;border-radius:50%;background:var(--white)}
.brand-name{font-family:"Nunito",sans-serif;font-weight:900;font-size:30px;color:var(--white);letter-spacing:.5px}

.account{left:860px;top:0;width:340px;height:52px;background:linear-gradient(var(--tab-tan),var(--tab-tan-dark));border-bottom-left-radius:22px;clip-path:polygon(8% 0,100% 0,100% 100%,0 100%)}
.out{left:826px;top:0;width:44px;height:44px;border-radius:50%;background:radial-gradient(circle at 40% 35%,#fff58a,var(--out-yellow) 60%,#e0a800);font-family:"Nunito",sans-serif;font-weight:900;font-size:14px;display:flex;align-items:center;justify-content:center;color:var(--ink);box-shadow:0 0 14px 4px rgba(255,240,140,.55)}
.welcome{left:888px;top:4px;font-family:"Nunito",sans-serif;font-weight:800;font-size:16px;color:var(--welcome-red)}
.welcome b{color:var(--white)}
.account-tab{top:31px;height:20px;background:var(--tab-blue);color:var(--white);font-family:"Nunito",sans-serif;font-weight:800;font-size:15px;display:flex;align-items:center;justify-content:center;clip-path:polygon(8% 0,100% 0,92% 100%,0 100%)}
.tab-settings{left:884px;width:152px}
.tab-help{left:1036px;width:124px}

.nav{left:6px;top:52px;width:1190px;height:33px;border-radius:10px;background:linear-gradient(var(--nav-yellow-light),var(--nav-yellow) 55%,#f2dc2a)}
.nav-item,.nav-sep{top:60px;font-family:"Nunito",sans-serif;font-weight:900;font-size:15px;color:var(--nav-text);letter-spacing:.4px}
.search{left:870px;top:57px;width:232px;height:25px;background:var(--white);border-radius:6px 3px 12px 3px;font-family:"Nunito",sans-serif;font-weight:900;font-size:15px;color:#444;padding:3px 14px}
.go{left:1104px;top:57px;width:36px;height:25px;background:var(--tab-blue);border-radius:8px 3px 8px 3px;color:var(--white);font-family:"Nunito",sans-serif;font-weight:900;font-size:14px;display:flex;align-items:center;justify-content:center}

.apps{left:800px;top:85px;width:400px;height:19px;background:var(--green);border-bottom-left-radius:4px}
.app-link{top:85px;font-family:"Nunito",sans-serif;font-weight:800;font-size:15px;color:var(--white)}

.panel{left:6px;top:124px;width:1193px;height:448px;border-radius:10px;overflow:hidden;background:linear-gradient(var(--row-gap) 55%,var(--panel-bottom))}
.panel-head{height:48px;background:linear-gradient(#9ac456,var(--green-dark));color:var(--white);font-family:"Nunito",sans-serif;font-weight:900;font-size:29px;padding:3px 18px}
.panel-meta{height:63px;background:var(--purple);position:relative;color:var(--white);font-size:13px}
.panel-meta span{position:absolute}
.row{position:absolute;left:0;width:100%;height:42px;background:var(--row);font-size:13px}
.row span{position:absolute;top:11px}

.copyright{left:14px;top:585px;color:var(--white);font-size:13px}
</style>
</head>
<body>
<header>
  <div class="abs brand"><span class="brand-dot"></span><span class="brand-name">skylark</span></div>
  <div class="abs account"></div>
  <div class="abs out">OUT</div>
  <div class="abs welcome">Welcome : <b>Student@lms.skylark.nl</b></div>
  <div class="abs account-tab tab-settings">Settings</div>
  <div class="abs account-tab tab-help">Help</div>

  <nav class="abs nav" aria-label="Main"></nav>
  <span class="abs nav-item" style="left:19px">HOME</span>
  <span class="abs nav-sep" style="left:98px">|</span>
  <span class="abs nav-item" style="left:133px">STUDY GUIDE</span>
  <span class="abs nav-sep" style="left:274px">|</span>
  <span class="abs nav-item" style="left:309px">BOOKS</span>
  <span class="abs nav-sep" style="left:397px">|</span>
  <span class="abs nav-item" style="left:431px">TESTS</span>
  <span class="abs nav-sep" style="left:513px">|</span>
  <span class="abs nav-item" style="left:548px">RESULTS</span>
  <div class="abs search">SEARCH</div>
  <div class="abs go">GO</div>

  <div class="abs apps"></div>
  <span class="abs app-link" style="left:806px">Postrix</span>
  <span class="abs app-link" style="left:875px">Calendar</span>
  <span class="abs app-link" style="left:968px">Documents</span>
  <span class="abs app-link" style="left:1080px">Sites</span>
  <span class="abs app-link" style="left:1146px">Chat</span>
</header>

<main class="abs panel">
  <h1 class="panel-head">Study guide Engels</h1>
  <div class="panel-meta">
    <span style="left:10px;top:7px">« Back &nbsp;Engels door leraar@lms.skylark.nl voor m2@lms.skylark.nl</span>
    <span style="left:803px;top:2px">English by Skylark</span>
    <span style="left:773px;top:23px">Eerste trimester (22-12-2010)</span>
    <span style="left:15px;top:45px">Assignment</span>
    <span style="left:238px;top:45px">Description</span>
    <span style="left:928px;top:45px">Deadline</span>
    <span style="left:1131px;top:45px">Mark</span>
  </div>
  <div class="row" style="top:117px"><span style="left:22px">Opdracht 1</span><span style="left:242px">Engels opdracht 1 door leraar@lms.skylark.nl voor m2@lms.skylark.nl</span><span style="left:931px">22-12-2010</span></div>
  <div class="row" style="top:179px"><span style="left:22px">Opdracht 1</span><span style="left:242px">Engels opdracht 1 door leraar@lms.skylark.nl voor m2@lms.skylark.nl</span><span style="left:931px">22-12-2010</span></div>
  <div class="row" style="top:240px"><span style="left:22px">Opdracht 1</span><span style="left:242px">Engels opdracht 1 door leraar@lms.skylark.nl voor m2@lms.skylark.nl</span><span style="left:931px">22-12-2010</span></div>
  <div class="row" style="top:301px"><span style="left:22px">Opdracht 1</span><span style="left:242px">Engels opdracht 1 door leraar@lms.skylark.nl voor m2@lms.skylark.nl</span><span style="left:931px">22-12-2010</span></div>
</main>

<footer class="abs copyright">Copyright © 2010-2010 Skylark</footer>
</body>
</html>
```